After a very formal and professional busuness card, After high qaulity for high end customers

Larkmere Bathrooms
0487265920
Lic # 582143K
Renovation specialists
Tobin@larkmerebathrooms.com.au

```html
<!DOCTYPE html>
<html lang="en">
<head>
<meta charset="utf-8">
<title>Larkmere Bathrooms – Business Card</title>
<link rel="stylesheet" href="https://fonts.googleapis.com/css2?family=Jost:wght@400;500&display=swap">
<style>
  :root {
    --stage: #666666;
    --card: #ffffff;
    --brand-blue: #0071bc;
    --soft-grey: #cacaca;
    --ink: #2b2b2b;
    --on-blue: #ffffff;
  }
  * { box-sizing: border-box; margin: 0; padding: 0; }
  html, body {
    width: 1000px; height: 1200px; overflow: hidden;
    background: var(--stage);
    font-family: "Jost", "Futura", sans-serif;
  }
  .card {
    position: absolute; left: 51px; width: 899px; height: 540px;
    background: var(--card); overflow: hidden;
  }
  .card--front { top: 43px; }
  .card--back { top: 617px; }
  .card__waves { position: absolute; inset: 0; width: 100%; height: 100%; }
  .wave--grey { fill: var(--soft-grey); }
  .wave--blue { fill: var(--brand-blue); }

  .header-name {
    position: absolute; right: 44px; top: 30px;
    font-size: 25px; font-weight: 400; color: var(--brand-blue);
  }
  .brand {
    position: absolute; display: flex; align-items: center; gap: 16px;
  }
  .brand__square { width: 34px; height: 34px; flex: none; }
  .brand__name { font-size: 46px; font-weight: 500; letter-spacing: 0.5px; line-height: 1; }
  .brand--front { left: 64px; top: 150px; }
  .brand--front .brand__square { background: var(--brand-blue); }
  .brand--front .brand__name { color: var(--brand-blue); }
  .brand--back { left: 0; right: 0; top: 248px; justify-content: center; }
  .brand--back .brand__square { background: var(--on-blue); }
  .brand--back .brand__name { color: var(--on-blue); }

  .contact {
    position: absolute; left: 396px; top: 340px; list-style: none;
    font-size: 25px; color: var(--ink); line-height: 1;
  }
  .contact__item { display: flex; align-items: center; height: 44px; }
  .contact__icon { width: 26px; height: 26px; margin-right: 10px; flex: none; }
  .contact__spacer { width: 26px; margin-right: 10px; flex: none; }
  .tagline {
    position: absolute; left: 52px; top: 489px;
    font-size: 25px; color: var(--on-blue); font-weight: 400;
  }
</style>
</head>
<body>
  <section class="card card--front">
    <svg class="card__waves" viewBox="0 0 899 540" preserveAspectRatio="none" aria-hidden="true">
      <path class="wave--grey" d="M0 0 H899 V67 C800 100 700 80 560 60 C420 40 300 15 180 25 C100 32 40 50 0 65 Z"/>
      <path class="wave--blue" d="M0 473 C60 452 140 450 230 458 C380 472 520 510 680 515 C780 518 850 495 899 476 V540 H0 Z"/>
    </svg>
    <p class="header-name">Larkmere Bathrooms</p>
    <div class="brand brand--front">
      <span class="brand__square"></span>
      <span class="brand__name">Larkmere Bathrooms</span>
    </div>
    <ul class="contact">
      <li class="contact__item"><span class="contact__spacer"></span>Lic # 582143K</li>
      <li class="contact__item">
        <svg class="contact__icon" viewBox="0 0 26 26" aria-hidden="true">
          <rect width="26" height="26" rx="3" fill="var(--brand-blue)"/>
          <path d="M8 6.5c1-.6 1.8-.4 2.3.5l1.2 2.3c.3.7.1 1.3-.5 1.7l-.9.6c.7 1.7 2 3.1 3.7 3.9l.6-.9c.4-.6 1.1-.8 1.7-.4l2.3 1.3c.8.5 1 1.3.4 2.2-.9 1.3-2.3 1.8-3.7 1.2-3.6-1.5-6.3-4.3-7.7-7.9-.5-1.5 0-3 .6-4.5z" fill="#fff"/>
        </svg>0487265920</li>
      <li class="contact__item">
        <svg class="contact__icon" viewBox="0 0 26 26" aria-hidden="true">
          <rect width="26" height="26" rx="3" fill="var(--brand-blue)"/>
          <rect x="5.5" y="8" width="15" height="10.5" fill="none" stroke="#fff" stroke-width="1.5"/>
          <path d="M5.5 8 L13 14 L20.5 8 M5.5 18.5 L11 13.2 M20.5 18.5 L15 13.2" fill="none" stroke="#fff" stroke-width="1.3"/>
        </svg>Tobin@larkmerebathrooms.com.au</li>
    </ul>
    <p class="tagline">Renovation specialists</p>
  </section>

  <section class="card card--back">
    <svg class="card__waves" viewBox="0 0 899 540" preserveAspectRatio="none" aria-hidden="true">
      <rect class="wave--blue" x="0" y="0" width="899" height="540"/>
      <path class="wave--grey" d="M0 0 H899 V64 C840 40 740 20 626 22 C500 25 380 55 260 75 C190 86 120 88 0 64 Z"/>
      <path fill="var(--card)" d="M0 475 C80 505 180 520 271 517 C420 512 560 462 700 455 C780 452 850 462 899 475 V540 H0 Z"/>
    </svg>
    <div class="brand brand--back">
      <span class="brand__square"></span>
      <span class="brand__name">Larkmere Bathrooms</span>
    </div>
  </section>
</body>
</html>
```